Seeking a beautiful packaging box for Dusk Haven - an essential oil blend (mock up provided!)

My sleep brand - Dusk Haven - is almost ready to go to market. And I need a box! Dusk Haven is a high end essential oils/sleep hygiene brand.

I need a gorgeous, classy box for our 3 sizes of essential oil product we are selling. I have a draft mockup which is to approximate size (attached), but need some help with the finishing touches and layout so it's really polished. I am looking for simple/monochrome designs using black and off white (think Verlin inspo!)

We are selling a 15mL dropper bottle and two roll ons (5ml, 10ml) of the essential oil blend. These are all amber bottles with black top. The box design will be almost identical for each, with very slight variations due to size differences.

The size of the boxes will be
15mL dropper: 30x30x95mm
10ml roller: 19x19x88mm
5ml roller: 18x18x59mm

Target Market(s)

High end/high price point product, shift workers, mums, people suffering stress and insomnia

Industry/Entity Type

Health And Wellness

Font styles to use
Serif
Sans Serif

Colors

Designer to choose only greyscale colors for use in the design.

Requirements
Must have
• I have attached a word document which includes all the necessary text:
- ingredients
- directions
- cautions
- info on essential oils/dusk haven (abbreviated on the smallest box)

Additionally:
- volume
- our website
- instagram logo/duskhavenau name
- made in australia
- recycle symbol
- 12 month open symbol
Nice to have
• I would like the boxes to be monochromatic: white or off white colour, with black logo and writing. I am open to variations on the logo (ie position of writing in relation to the circle/change of font size), but mostly need help with layout, font, direction of text, design of the blank spaces, patterns etc.
Should not have
• Colours

```html
<!DOCTYPE html>
<html lang="en">
<head>
<meta charset="utf-8">
<title>Dusk Haven – Roll on Essential Oil Blend Box</title>
<link rel="stylesheet" href="https://fonts.googleapis.com/css2?family=Marcellus&family=Pinyon+Script&family=Arimo:wght@400;700&display=swap">
<style>
  :root {
    --page: #e6e6e4;
    --paper: #f4f2ed;
    --paper-side: #ebe8e2;
    --ink: #161616;
    --ink-soft: #3a3a3a;
    --rule: #8d8d8d;
    --photo-top: #f4f2ed;
    --photo-mid: #cfcdc8;
    --photo-low: #a9a7a2;
    --band: #161616;
    --band-ink: #f4f2ed;
  }
  * { box-sizing: border-box; margin: 0; padding: 0; }
  html, body { width: 900px; height: 1200px; overflow: hidden; background: var(--page); }
  .canvas {
    width: 900px; height: 1200px;
    display: flex; justify-content: center; align-items: center;
  }
  .box-net { display: flex; height: 1060px; box-shadow: 0 0 0 1px #d0cec9; }

  /* Side panel: all content runs top to bottom, rotated */
  .side-panel {
    position: relative; width: 130px; height: 100%;
    background: var(--paper-side); color: var(--ink);
    border-right: 1px solid #d6d3cc;
    overflow: hidden;
  }
  .side-strip {
    position: absolute; top: 40px; left: 120px;
    width: 980px; height: 110px;
    transform-origin: top left; transform: rotate(90deg);
    display: flex; gap: 18px;
    font-family: "Arimo", sans-serif; font-size: 8.6px; line-height: 11px;
    color: var(--ink-soft);
  }
  .side-block { flex: none; }
  .side-block h2 {
    font-family: "Arimo", sans-serif; font-size: 9px; font-weight: 700;
    letter-spacing: 0.8px; color: var(--ink); margin-bottom: 3px;
  }
  .block-ingredients { width: 360px; }
  .block-directions { width: 200px; }
  .block-cautions { width: 200px; }
  .block-info {
    width: 166px; display: flex; flex-direction: column; justify-content: space-between;
  }
  .side-icons { display: flex; gap: 14px; align-items: flex-end; }
  .side-icons svg { stroke: var(--ink); fill: none; stroke-width: 1.4; }
  .open-period { font-size: 8px; font-weight: 700; fill: var(--ink); stroke: none; }
  .contact { font-size: 9px; line-height: 13px; color: var(--ink); }

  /* Front panel */
  .front-panel {
    position: relative; width: 310px; height: 100%;
    background: var(--paper); color: var(--ink);
    display: flex; flex-direction: column; align-items: center;
  }
  .brand-mark {
    margin-top: 120px; width: 120px; height: 120px;
    border: 4px solid var(--ink); border-radius: 50%;
  }
  .brand-name { margin-top: 48px; text-align: center; font-family: "Marcellus", serif; font-weight: 400; }
  .brand-name .line-one { display: block; font-size: 52px; letter-spacing: 4px; line-height: 1; }
  .brand-name .line-two { display: block; font-size: 21px; letter-spacing: 9px; margin-top: 14px; padding-left: 9px; }
  .product-type { margin-top: 58px; text-align: center; font-family: "Pinyon Script", cursive; color: var(--ink-soft); }
  .product-type .format {
    display: flex; align-items: center; justify-content: center; gap: 10px; font-size: 24px;
  }
  .product-type .format::before,
  .product-type .format::after { content: ""; width: 32px; height: 2px; background: var(--ink-soft); }
  .product-type .blend { display: block; font-size: 26px; margin-top: 8px; }
  .photo-area {
    position: absolute; left: 0; right: 0; top: 560px; bottom: 94px;
    background: linear-gradient(180deg, var(--photo-top) 0%, var(--photo-mid) 40%, var(--photo-mid) 60%, var(--photo-low) 100%);
  }
  .info-band {
    position: absolute; left: 0; right: 0; bottom: 0; height: 94px;
    background: var(--band); color: var(--band-ink);
    display: flex; flex-direction: column; align-items: center; justify-content: center;
    font-family: "Arimo", sans-serif; font-size: 21px; line-height: 28px;
  }
</style>
</head>
<body>
<div class="canvas">
  <div class="box-net">
    <section class="side-panel" aria-label="Side panel">
      <div class="side-strip">
        <div class="side-block block-ingredients">
          <h2>INGREDIENTS:</h2>
          <p>Lavandula Angustifolia (Australian Lavender), Vetiveria Zizanoides (Vetiver) Root Oil, Sweet Vanilla Fragrant Oil, Pelargonium Capitatum (Cape Rose Geranium) Leaf Extract, Juniperus Virginiana (Cedarwood) Wood Oil, Citrus Limon (Australian Lemon) Peel Oil, Origanum Majorana (Marjoram) Leaf Oil, Cananga Odorata (Ylang Ylang) Flower Oil, Anthemis Nobilis (Roman Chamomile) Flower Oil</p>
        </div>
        <div class="side-block block-directions">
          <h2>DIRECTIONS:</h2>
          <p>Roll onto wrists, temples and behind the ears 30 minutes before bed. Breathe deeply and relax. Reapply as needed through the night.</p>
        </div>
        <div class="side-block block-cautions">
          <h2>CAUTIONS:</h2>
          <p>For external use only. Avoid contact with eyes. Patch test before use. Not for use on children under 2 years. Consult a doctor if pregnant. Keep out of reach of children.</p>
        </div>
        <div class="side-block block-info">
          <div class="side-icons">
            <svg class="icon-recycle" width="34" height="34" viewBox="0 0 34 34" aria-label="Recyclable">
              <path d="M11 12 L17 3 L23 12"/><path d="M20 11 L23 12 L24 9"/>
              <path d="M27 16 L31 26 L21 26"/><path d="M23 23 L21 26 L24 28"/>
              <path d="M13 26 L3 26 L8 17"/><path d="M5 18 L8 17 L9 20"/>
            </svg>
            <svg class="icon-open-jar" width="32" height="34" viewBox="0 0 32 34" aria-label="12 months after opening">
              <path d="M4 14 H26 V32 H4 Z"/><path d="M6 10 L22 2"/>
              <text class="open-period" x="7" y="27">12M</text>
            </svg>
          </div>
          <p class="contact">duskhaven.com.au<br>@duskhavenau</p>
        </div>
      </div>
    </section>

    <section class="front-panel" aria-label="Front panel">
      <div class="brand-mark"></div>
      <h1 class="brand-name"><span class="line-one">DUSK</span><span class="line-two">HAVEN</span></h1>
      <p class="product-type">
        <span class="format">Roll on</span>
        <span class="blend">Essential Oil Blend</span>
      </p>
      <div class="photo-area" role="img" aria-label="Soft monochrome photograph of a mother and child asleep together in bed"></div>
      <div class="info-band">
        <span class="origin">Made in Australlia</span>
        <span class="volume">15ml</span>
      </div>
    </section>
  </div>
</div>
</body>
</html>
```